A new PowerPoint Template for a French consulting company

Who are we?

Formed in 2005, Quorv is a consulting company specialising in the human aspect of change and transformation.

From our offices in the heart of Paris, our team of 30 consultants work with leading organisations in the Aerospace, Finance, Transportation and Public sectors to deliver lasting change.

Our customers trust us with some of their most strategic and sensitive projects. They trust us with these projects because:
- We listen to them, ensuring we understand the real needs of their business
- We involve them, co-developing and tailoring our solutions to the specific challenges they face
- We’re professional, without taking ourselves too seriously
- We’re imaginative, whilst always remaining pragmatic
- We get results!

You can find out more about who we are and the work we do here: http://www.quorv-example.fr/en

What we need from you?

We’re approaching our 10th birthday and, whilst we still love what we do, we think it’s the right time to update our image.

We’d like you to design us a new PowerPoint template, that will be used for all of our internal and client facing work. You can base your submissions on our existing logo and colour scheme (see files attached) or you can submit your own fresh ideas – after all, we’re not afraid of change!

Finally, whilst we’re looking for you to be creative, there are some simple guidelines that we need you to keep in mind:

1. The Template needs to include both a front cover and a “content” page

2. The front cover needs to:
- Include our logo
- Reflect “who we are” and the type of work that we do

3. The content page needs to:
- Have a predominantly white background
- Be practical to use, making an effective use of the 4:3 standard PPT size
- Include an area across the top of the page for the slide title
- Include areas along the bottom of the page for the page number and date

4. If you decide to propose a new colour scheme, it should be balanced and the “accents” usable

5. The PowerPoint Template needs to be “printer friendly”

6. The fonts you use should be standard

What we don’t want?

To give you as much help as possible, here are some things that we really don’t want:

- Submissions that are dull grey or navy blue, suggesting we’re nothing but boring corporate suits
- Submissions that are Lulette pink or too “soft and cuddly”
- Submissions that use lots of stock images of “happy, smiling, consultants”
- Submissions that will be the height of fashion today, but completely out of date next year

```html
<!DOCTYPE html>
<html lang="en">
<head>
<meta charset="utf-8">
<title>Quorv – Presentation Template</title>
<link href="https://fonts.googleapis.com/css2?family=Roboto+Condensed:wght@300;400;700&display=swap" rel="stylesheet">
<style>
  :root {
    --stage: #6a6a6a;
    --stage-dark: #555555;
    --paper: #ffffff;
    --paper-grey: #e6e6e6;
    --teal: #1fb3a0;
    --teal-light: #5fd3c4;
    --teal-deep: #00755a;
    --teal-bright: #2fd6bd;
    --mint: #b6f5ea;
    --plum: #6b0f3a;
    --text-grey: #8c8c8c;
    --date-grey: #a9c9c3;
  }
  * { box-sizing: border-box; margin: 0; padding: 0; }
  html, body { width: 1200px; height: 1000px; overflow: hidden; }
  body {
    background: radial-gradient(ellipse at center, var(--stage) 0%, var(--stage-dark) 100%);
    font-family: "Roboto Condensed", "Arial Narrow", sans-serif;
    position: relative;
  }
  .slide {
    position: absolute;
    width: 528px;
    height: 396px;
    overflow: hidden;
    box-shadow: 2px 3px 6px rgba(0,0,0,0.45);
  }
  .slide--cover { left: 47px; top: 82px; background: linear-gradient(180deg, #f2f2f2, var(--paper)); }
  .slide--content { left: 624px; top: 82px; background: linear-gradient(180deg, var(--paper) 60%, #e9e9e9 100%); }
  .slide--closing { left: 354px; top: 540px; background: linear-gradient(180deg, var(--paper) 70%, #dcdcdc 100%); }

  .decor { position: absolute; left: 0; right: 0; }
  .decor--cover {
    top: 0; height: 300px;
    background: linear-gradient(105deg, var(--teal-light) 0%, var(--teal) 40%, var(--teal-deep) 80%);
  }
  .decor--content-top {
    top: 0; height: 40px;
    background: linear-gradient(90deg, var(--mint) 0%, var(--teal-bright) 55%, var(--teal-deep) 100%);
  }
  .decor--content-bottom {
    bottom: 0; height: 36px;
    background: linear-gradient(90deg, #4fbfae 0%, var(--teal) 60%, #6ad9c8 100%);
  }
  .decor--closing {
    top: 0; height: 290px;
    background: linear-gradient(110deg, var(--teal-bright) 0%, #12b096 50%, #0e8f7a 100%);
  }

  .wordmark {
    position: absolute;
    color: var(--plum);
    font-weight: 400;
    letter-spacing: -0.5px;
    line-height: 1;
  }
  .cover-heading {
    position: absolute;
    right: 20px;
    top: 86px;
    text-align: right;
    line-height: 1;
  }
  .cover-date { color: var(--date-grey); font-size: 12px; font-weight: 700; letter-spacing: 0.3px; }
  .cover-title { color: #ffffff; font-size: 28px; font-weight: 300; margin-top: 3px; }
  .cover-subtitle { color: var(--teal); font-size: 28px; font-weight: 300; }
  .cover-wordmark { left: 26px; bottom: 34px; font-size: 38px; }
  .cover-url {
    position: absolute; right: 20px; bottom: 16px;
    color: var(--plum); font-size: 11px; font-weight: 700; letter-spacing: 0.3px;
  }

  .content-title {
    position: absolute; left: 44px; top: 80px;
    color: var(--teal); font-size: 28px; font-weight: 300; line-height: 1.1;
  }
  .content-body {
    position: absolute; left: 44px; top: 127px; width: 440px;
    color: var(--text-grey); font-size: 11.5px; line-height: 1.25;
  }
  .content-body p + p { margin-top: 14px; }
  .content-footer {
    position: absolute; left: 14px; bottom: 6px;
    display: flex; align-items: center; gap: 14px;
    color: #ffffff; font-size: 8.5px;
  }
  .footer-divider { width: 1px; height: 24px; background: var(--plum); transform: rotate(20deg); }
  .content-wordmark { right: 14px; bottom: 26px; font-size: 26px; }

  .closing-heading {
    position: absolute; left: 0; right: 0; top: 136px;
    text-align: center; color: #ffffff; font-size: 58px; font-weight: 300;
  }
  .closing-address {
    position: absolute; left: 0; right: 0; top: 312px;
    text-align: center; color: var(--text-grey); font-size: 9.5px; line-height: 1.2;
    font-style: normal;
  }
  .closing-url {
    position: absolute; left: 0; right: 0; top: 360px;
    text-align: center; color: var(--teal-deep); font-size: 10px; font-weight: 700;
  }
</style>
</head>
<body>

<section class="slide slide--cover">
  <div class="decor decor--cover" role="img" aria-label="Decorative translucent teal backdrop"></div>
  <div class="cover-heading">
    <div class="cover-date">SEPTEMBER 14, 2014</div>
    <div class="cover-title">PRESENTATION</div>
    <div class="cover-subtitle">TITLE</div>
  </div>
  <div class="wordmark cover-wordmark">Quorv</div>
  <div class="cover-url">WWW.QUORV-EXAMPLE.FR</div>
</section>

<section class="slide slide--content">
  <div class="decor decor--content-top" role="img" aria-label="Decorative teal header band"></div>
  <div class="decor decor--content-bottom" role="img" aria-label="Decorative teal footer band"></div>
  <h1 class="content-title">ABOUT US</h1>
  <div class="content-body">
    <p>Quorv, a consulting firm specializing in change management, helps major organizations to design and implement their transformation programs.</p>
    <p>Quorv has developed quickly since its creation in 2005, due to major and continuing private and public clients in industrial and service sectors.</p>
    <p>Quorv works mainly in Europe.</p>
    <p>Quorv offers all the different steps of a transformation program, from conception to implementation.</p>
    <p>Shared by all consultants, these convictions are the primary success factors in Quorv's interventions.</p>
  </div>
  <div class="content-footer">
    <span>SEPTEMBER 14, 2014</span>
    <span class="footer-divider"></span>
    <span>ABOUT US</span>
  </div>
  <div class="wordmark content-wordmark">Quorv</div>
</section>

<section class="slide slide--closing">
  <div class="decor decor--closing" role="img" aria-label="Decorative translucent teal backdrop"></div>
  <div class="closing-heading">THANK YOU!</div>
  <address class="closing-address">
    24 rue Lamarck<br>
    75018 Paris - France<br>
    +33 (0) 1 42 00 18 36
  </address>
  <div class="closing-url">www.quorv-example.fr</div>
</section>

</body>
</html>
```